Business Card Design Project

See the detainl of the Fernlo company project I also have live: http://tasks.plomwerk.com/task.aspx?id=384920

Reason: I am waiting to select a logo design and ideally the business card design will be from the same person

```html
<!DOCTYPE html>
<html lang="en">
<head>
<meta charset="utf-8">
<title>Tavrin LLP – Business Card</title>
<link rel="stylesheet" href="https://fonts.googleapis.com/css2?family=Lato:wght@400;700;900&display=swap">
<style>
  :root {
    --bg: #e6e7e8;
    --card: #fbfbfb;
    --ink: #3d4a55;
    --band: #36434d;
    --green: #7ab82f;
    --white: #ffffff;
  }
  html, body {
    margin: 0;
    padding: 0;
    width: 1200px;
    height: 1000px;
    overflow: hidden;
    background: var(--bg);
  }
  .canvas {
    position: relative;
    width: 1200px;
    height: 1000px;
    font-family: "Lato", Arial, sans-serif;
  }
  .card {
    position: absolute;
    left: 320px;
    top: 65px;
    width: 560px;
    height: 870px;
    background: var(--card);
    box-shadow: 0 6px 24px rgba(0,0,0,0.12);
    overflow: hidden;
  }
  .brand {
    position: absolute;
    left: 60px;
    top: 95px;
    display: flex;
    align-items: flex-end;
    gap: 14px;
  }
  .brand-name {
    font-weight: 900;
    font-size: 92px;
    line-height: 1;
    letter-spacing: -2px;
    color: var(--ink);
  }
  .brand-name small {
    font-size: 30px;
    letter-spacing: 0;
  }
  .brand-square {
    width: 26px;
    height: 26px;
    background: var(--green);
    margin-bottom: 12px;
  }
  .person {
    position: absolute;
    left: 60px;
    top: 250px;
  }
  .person-name {
    font-weight: 700;
    font-size: 44px;
    color: var(--ink);
    margin: 0;
    line-height: 1.1;
  }
  .person-title {
    font-weight: 700;
    font-size: 24px;
    color: var(--green);
    margin: 6px 0 0 150px;
  }
  .divider {
    position: absolute;
    left: 0;
    top: 395px;
    width: 355px;
    height: 4px;
    background: var(--green);
  }
  .contacts {
    position: absolute;
    left: 45px;
    top: 425px;
    margin: 0;
    padding: 0;
    list-style: none;
    font-size: 29px;
    line-height: 40px;
    color: var(--ink);
  }
  .contacts .label {
    color: var(--green);
    font-size: 22px;
  }
  .band {
    position: absolute;
    left: 0;
    bottom: 0;
    width: 100%;
    height: 245px;
    background: var(--band);
    color: var(--white);
    box-sizing: border-box;
    padding: 26px 45px;
    font-size: 29px;
    line-height: 40px;
  }
  .band address {
    font-style: normal;
  }
  .band .web {
    color: var(--green);
    margin-top: 4px;
  }
</style>
</head>
<body>
<div class="canvas">
  <article class="card">
    <div class="brand">
      <span class="brand-name">Tavrin<small>,LLP</small></span>
      <span class="brand-square" aria-hidden="true"></span>
    </div>

    <div class="person">
      <h1 class="person-name">Alec Morrow</h1>
      <p class="person-title">title</p>
    </div>

    <div class="divider" aria-hidden="true"></div>

    <ul class="contacts">
      <li><span class="label">TEL:</span> +44 (0) 1632960418</li>
      <li><span class="label">FAX:</span> (0) 1632 960419</li>
      <li><span class="label">MOBILE:</span> +44 (0)7700 900XX</li>
      <li><span class="label">EMAIL:</span> alec.morrow@tavrin.co.uk</li>
    </ul>

    <footer class="band">
      <address>Alder Court,7B Millbrook Rd,<br>Granton, GT4 2LK</address>
      <div class="web">www.tavrin.co.uk</div>
    </footer>
  </article>
</div>
</body>
</html>
```